Professional Lighting Providers - Web Design

We need a web design to showcase our ability to provide lighting design and equipment to those who are in need of lighting equipment.

Our 4 markets are:
Broadcasting - Public and Commercial
Education - ISD wide, and private schools
Government - National News, Chamber videos, Press Releases
Religious - Sermon Recording, etc.

We provide lighting products, design consultations(how lights are setup and such), and custom light work.

We want the home page to be setup in a way that someone in one of the 4 markets can drill down into the site. Meaning they are greeted on the home page with 4 large icons or pictures for each market and then they can go farther into the site. We also want a top navigation to be preset so people who are just looking for lighting can also browse our products.

Logo colors are not as they appear on our current website.
#383388 is our current logo color, please also see attachment of logo. In addition, we are just "Bright Harbor - Lighting Systems". We dropped the RJ7 out of our name so please don't use it in the concept.

Our Current Site is http://rj7-example.com/index.asp.
We don't have set colors but we know we do not want reds or yellows.

The design should be simple, not cluttered, and not artsy, not fun, but very serious.

Requirements
Must have
• Image banner/slider at the top that slides our 4 products.
Also need to have a form on the home page that will convert visitors to subscribers for a newsletter. Also on every page we want a form were people can send an email off to us asking questions.

```html
<!DOCTYPE html>
<html lang="en">
<head>
<meta charset="utf-8">
<title>Bright Harbor - Lighting Systems</title>
<link href="https://fonts.googleapis.com/css2?family=Rufina:wght@700&family=Ubuntu:wght@400;500&family=Arimo:wght@400;700&display=swap" rel="stylesheet">
<style>
:root{
  --brand:#383388;
  --brand-deep:#241c78;
  --brand-mid:#4536c4;
  --ink:#333;
  --muted:#888;
  --line:#bbb;
  --page:#fff;
}
*{margin:0;padding:0;box-sizing:border-box}
html,body{width:943px;height:1200px;overflow:hidden;background:var(--page);font-family:Arimo,Arial,sans-serif;color:var(--ink)}
.page{position:relative;width:943px;height:1200px;overflow:hidden}
.abs{position:absolute}

.utility{right:54px;top:7px;display:flex;gap:10px;font-size:11px;font-weight:700;color:#333}
.utility span::before{content:"";display:inline-block;border-left:4px solid var(--brand);border-top:3px solid transparent;border-bottom:3px solid transparent;margin-right:6px;vertical-align:1px}
.utility i{font-style:normal;color:#666;font-weight:400}
.navbar{left:0;top:30px;width:943px;height:32px;background:linear-gradient(#5b4ed6,var(--brand-deep))}
.nav{left:382px;top:30px;height:36px;display:flex;font-family:Ubuntu,sans-serif;font-size:11px;color:#fff}
.nav a{padding:0 19px;line-height:34px;color:#fff;text-decoration:none}
.nav a.current{background:linear-gradient(#555,#222);padding:0 23px}
.logo{left:48px;top:-6px;width:180px;height:107px;border-radius:50%;background:radial-gradient(#fff 60%,#e4e4e4);box-shadow:0 2px 4px rgba(0,0,0,.15);text-align:center}
.logo .name{margin-top:34px;font-family:Ubuntu,sans-serif;font-weight:500;font-size:15px;color:var(--brand)}
.logo .name::before{content:"";display:inline-block;width:10px;height:10px;background:var(--brand);border-radius:50%;margin-right:5px}
.logo .sub{font-size:11px;letter-spacing:1.5px;color:#333;margin-top:3px}
.search{left:685px;top:76px;width:180px;height:24px;border:1px solid #ddd;border-radius:12px;font-size:10px;color:#aaa;padding:5px 10px}
.search-btn{left:869px;top:73px;width:29px;height:29px;border-radius:50%;background:radial-gradient(circle at 40% 35%,#7a6cf0,var(--brand-deep))}
.headline{left:0;top:104px;width:943px;text-align:center;font-family:Rufina,serif;font-size:26px;color:var(--brand);letter-spacing:1px}

.stage{left:0;top:350px;width:943px;height:112px;background:linear-gradient(var(--brand-mid),var(--brand-deep))}
.stage-shadow{left:80px;top:462px;width:790px;height:10px;background:radial-gradient(ellipse at top,rgba(0,0,0,.18),transparent 70%)}
.arrow{width:34px;height:34px;border:3px solid #999;border-radius:50%;background:#fff}

.market{top:498px;width:170px}
.market h2{font-family:Ubuntu,sans-serif;font-weight:500;font-size:16px;color:var(--brand);display:flex;align-items:center;gap:6px;margin-bottom:10px}
.hex{width:22px;height:22px;background:var(--brand);clip-path:polygon(25% 5%,75% 5%,100% 50%,75% 95%,25% 95%,0 50%);display:inline-block}
.thumb{width:168px;height:84px;border:3px solid #fff;box-shadow:0 0 0 1px #ccc}
.market p{font-size:10.5px;line-height:15.5px;color:#444;margin-top:8px;text-align:justify;letter-spacing:.3px}
.market p b{color:#222}
.more{display:block;text-align:right;font-size:8.5px;color:var(--brand);margin-top:6px}
.vrule{top:508px;height:180px;border-left:1px dotted var(--line)}
.hrule{left:62px;top:710px;width:832px;border-top:1px dotted #999}

.card{top:735px;width:190px;height:78px;padding:10px 14px;background:linear-gradient(90deg,#fff,#fff 80%,#f3f3f3);box-shadow:4px 4px 6px rgba(0,0,0,.08)}
.card h3{font-family:Ubuntu,sans-serif;font-weight:400;font-size:16px;color:var(--brand);white-space:nowrap}
.card p{font-size:10px;color:var(--muted);line-height:15px;margin-top:6px;letter-spacing:.4px}
.card .tag{position:absolute;right:-4px;bottom:10px;width:22px;height:14px;background:var(--brand);clip-path:polygon(30% 0,100% 0,100% 100%,30% 100%,0 50%);color:#fff;font-size:10px;line-height:14px;text-align:right;padding-right:5px}
.card .hex{position:absolute;right:2px;top:-6px;width:20px;height:20px}

.quick{left:697px;top:724px;width:190px;height:105px;background:linear-gradient(var(--brand-mid),var(--brand-deep));color:#fff;padding:5px 10px}
.quick h3{font-family:Ubuntu,sans-serif;font-weight:400;font-size:16px}
.quick h3 b{font-weight:500}
.quick li{list-style:none;font-family:Ubuntu,sans-serif;font-size:11px;margin-top:8px;display:flex;align-items:center;gap:10px}

.sidebar-rule{left:685px;top:724px;height:296px;border-left:3px solid #f1f1f1}
.enquiry-title{left:703px;top:844px;font-family:Ubuntu,sans-serif;font-size:16px;color:#555}
.enquiry-title b{font-weight:500;color:#444}
.field{left:700px;width:184px;height:24px;border:2px solid #e5e5e5;border-radius:12px;font-size:10px;color:#555;padding:4px 12px}
.submit{left:825px;top:992px;width:59px;height:19px;border-radius:10px;background:linear-gradient(var(--brand-mid),var(--brand-deep));color:#fff;font-family:Ubuntu,sans-serif;font-size:12px;text-align:center;line-height:19px}

.benefits-title{left:62px;top:860px;font-family:Ubuntu,sans-serif;font-size:18px;color:#444}
.benefits-title b{font-weight:400;color:var(--brand)}
.benefits{left:53px;top:897px;width:607px;height:93px;border-radius:10px;background:linear-gradient(#fafafa,#e8e8e8);box-shadow:0 1px 3px rgba(0,0,0,.15)}
.benefit{font-family:Ubuntu,sans-serif;font-size:12.5px;color:#444}
.benefit::before{content:"";display:inline-block;width:6px;height:6px;border-radius:50%;background:var(--brand);margin-right:11px;vertical-align:2px}

.footer{left:0;top:1033px;width:943px;height:167px;background:repeating-linear-gradient(0deg,#e9e9e9 0 1px,#f2f2f2 1px 3px)}
.fcol h4{font-family:Ubuntu,sans-serif;font-weight:400;font-size:15px;color:#666;display:flex;align-items:center;gap:5px;margin-bottom:8px}
.fcol h4 .hex{width:17px;height:17px;background:#777}
.fcol p{font-size:10px;line-height:15.5px;color:#666;letter-spacing:.4px}
.social{top:1061px;width:50px;text-align:center;font-size:9.5px;color:#555}
.social .ic{width:20px;height:20px;background:#777;border-radius:3px;margin:0 auto 5px}
.legal-rule{left:53px;top:1152px;width:832px;border-top:1px solid #ddd}
.legal{left:0;top:1170px;width:943px;text-align:center;font-size:9px;color:#444}
.legal span{margin:0 6px}
</style>
</head>
<body>
<div class="page">

  <div class="abs navbar"></div>
  <nav class="abs nav">
    <a class="current">Home</a><a>About us</a><a>Products</a><a>Lighting Design/Quote Request</a><a>Latest News</a>
  </nav>
  <div class="abs utility"><span>Manuals</span><i>|</i><span>Technicals</span><i>|</i><span>Contact us</span></div>
  <div class="abs logo"><div class="name">Bright Harbor</div><div class="sub">Lighting Systems</div></div>

  <div class="abs search">-----------Search--------------</div>
  <div class="abs search-btn">
    <svg width="29" height="29" viewBox="0 0 29 29"><circle cx="13" cy="13" r="5" fill="none" stroke="#fff" stroke-width="2.5"/><line x1="17" y1="17" x2="21" y2="21" stroke="#fff" stroke-width="3" stroke-linecap="round"/></svg>
  </div>

  <h1 class="abs headline">Real Solution To Studio Lighting</h1>

  <div class="abs stage"></div>
  <div class="abs stage-shadow"></div>
  <svg class="abs" style="left:0;top:140px" width="943" height="300" viewBox="0 0 943 300">
    <defs>
      <linearGradient id="g1" x1="0" x2="1"><stop offset="0" stop-color="#6b2fa0"/><stop offset="1" stop-color="#2c2c6a"/></linearGradient>
      <linearGradient id="g2" x1="0" y1="0" x2="0" y2="1"><stop offset="0" stop-color="#e8c48a"/><stop offset=".5" stop-color="#8a4a20"/><stop offset="1" stop-color="#3a1a0a"/></linearGradient>
      <radialGradient id="g3" cx=".5" cy=".45" r=".6"><stop offset="0" stop-color="#f2d6f0"/><stop offset=".35" stop-color="#b43a9a"/><stop offset="1" stop-color="#1a0810"/></radialGradient>
      <linearGradient id="g4" x1="0" y1="0" x2="0" y2="1"><stop offset="0" stop-color="#3fb3f0"/><stop offset=".6" stop-color="#0a4fb5"/><stop offset="1" stop-color="#051a40"/></linearGradient>
      <linearGradient id="g5" x1="0" y1="0" x2="0" y2="1"><stop offset="0" stop-color="#d8d8d8"/><stop offset="1" stop-color="#222"/></linearGradient>
    </defs>
    <polygon points="100,5 162,22 162,262 100,285" fill="url(#g1)" stroke="#fff" stroke-width="2" role="img" aria-label="Lit stage wall photo"/>
    <polygon points="162,5 302,55 302,265 162,290" fill="url(#g2)" stroke="#fff" stroke-width="3" role="img" aria-label="Hotel lobby lighting photo"/>
    <rect x="318" y="5" width="310" height="284" fill="url(#g3)" stroke="#fff" stroke-width="3" role="img" aria-label="Concert stage lighting photo"/>
    <polygon points="641,52 783,5 783,290 641,265" fill="url(#g4)" stroke="#fff" stroke-width="3" role="img" aria-label="Lighting console under blue beams photo"/>
    <polygon points="783,22 845,5 845,285 783,262" fill="url(#g5)" stroke="#fff" stroke-width="2" role="img" aria-label="Performer poster photo"/>
  </svg>
  <div class="abs arrow" style="left:51px;top:270px"><svg width="28" height="28" viewBox="0 0 28 28"><polygon points="17,8 9,14 17,20" fill="#999"/></svg></div>
  <div class="abs arrow" style="left:859px;top:270px"><svg width="28" height="28" viewBox="0 0 28 28"><polygon points="11,8 19,14 11,20" fill="#999"/></svg></div>

  <section class="abs market" style="left:80px">
    <h2><span class="hex"></span>Broadcasting</h2>
    <div class="thumb" role="img" aria-label="News studio set photo" style="background:linear-gradient(#2d4aa8,#8a6a40)"></div>
    <p><b>The roots of Bright Harbor Lighting Products</b> date back to 1975 when Bright Harbor Lighting was formed,</p>
    <span class="more">READ MORE..</span>
  </section>
  <div class="abs vrule" style="left:265px"></div>
  <section class="abs market" style="left:277px">
    <h2><span class="hex"></span>Education</h2>
    <div class="thumb" role="img" aria-label="Classroom photo" style="background:linear-gradient(#d8d2c0,#7a5a30)"></div>
    <p><b>The roots of Bright Harbor Lighting Products</b> date back to 1975 when Bright Harbor Lighting was formed,</p>
    <span class="more">READ MORE..</span>
  </section>
  <div class="abs vrule" style="left:465px"></div>
  <section class="abs market" style="left:481px">
    <h2><span class="hex"></span>Government</h2>
    <div class="thumb" role="img" aria-label="Capitol building at dusk photo" style="background:linear-gradient(#6a88c8,#1a2850)"></div>
    <p><b>The roots of Bright Harbor Lighting Products</b> date back to 1975 when Bright Harbor Lighting was formed,</p>
    <span class="more">READ MORE..</span>
  </section>
  <div class="abs vrule" style="left:671px"></div>
  <section class="abs market" style="left:687px">
    <h2><span class="hex"></span>Religious</h2>
    <div class="thumb" role="img" aria-label="Church with lit tree at night photo" style="background:linear-gradient(#8a3a1a,#2a1a10)"></div>
    <p><b>The roots of Bright Harbor Lighting Products</b> date back to 1975 when Bright Harbor Lighting was formed,</p>
    <span class="more">READ MORE..</span>
  </section>
  <div class="abs hrule"></div>

  <div class="abs card" style="left:51px"><h3>About Bright Harbor</h3><p>The roots of Bright Harbor Lighting Products date</p><span class="hex"></span><span class="tag">+</span></div>
  <div class="abs card" style="left:264px"><h3>Featured Products</h3><p>The roots of Bright Harbor Lighting Products date</p><span class="hex"></span><span class="tag">+</span></div>
  <div class="abs card" style="left:480px"><h3>Our Products</h3><p>The roots of Bright Harbor Lighting Products date</p><span class="hex"></span><span class="tag">+</span></div>

  <div class="abs sidebar-rule"></div>
  <div class="abs quick">
    <h3>Quick <b>Links</b></h3>
    <ul>
      <li><svg width="13" height="11" viewBox="0 0 13 11"><polyline points="1,6 5,10 12,1" fill="none" stroke="#fff" stroke-width="2.5"/></svg>Fixture Cutsheets</li>
      <li><svg width="13" height="11" viewBox="0 0 13 11"><polyline points="1,6 5,10 12,1" fill="none" stroke="#fff" stroke-width="2.5"/></svg>Cost Savings Calculator</li>
      <li><svg width="13" height="11" viewBox="0 0 13 11"><polyline points="1,6 5,10 12,1" fill="none" stroke="#fff" stroke-width="2.5"/></svg>Customer List</li>
    </ul>
  </div>

  <div class="abs enquiry-title">Quick <b>Enquery</b></div>
  <div class="abs field" style="top:875px">---- Name -----</div>
  <div class="abs field" style="top:906px">---- Email -----</div>
  <div class="abs field" style="top:937px;height:45px">---- Your requirement details -----</div>
  <div class="abs submit">Submit</div>

  <div class="abs benefits-title"><b>Benefits of Bright Harbor</b> Lighting Fluorescents</div>
  <div class="abs benefits"></div>
  <div class="abs benefit" style="left:70px;top:922px">Cooler</div>
  <div class="abs benefit" style="left:70px;top:948px">Spectacular images</div>
  <div class="abs benefit" style="left:256px;top:923px">Lower Operating Cost</div>
  <div class="abs benefit" style="left:256px;top:949px">Total Control</div>
  <div class="abs benefit" style="left:440px;top:923px">Broad Selection</div>
  <div class="abs benefit" style="left:440px;top:949px">No Flicker or Noice Made In us</div>

  <div class="abs footer"></div>
  <div class="abs fcol" style="left:53px;top:1043px;width:160px">
    <h4><span class="hex"></span>Latest News</h4>
    <p><b>Same price as the 3CT210, but</b><br>- more light output<br>- more even distribution of light<br>- lighter aluminum construction<br>- semi-specular reflector</p>
  </div>
  <div class="abs fcol" style="left:245px;top:1043px;width:200px">
    <h4><span class="hex"></span>Testimonial</h4>
    <p style="text-align:justify">The most complete line of fluorescent lighting fixtures to meet all of your studio/video lighting needs: accent, fill, video-conference, small studio, distance learning, worship, and more.</p>
  </div>
  <div class="abs fcol" style="left:484px;top:1043px;width:180px">
    <h4><span class="hex"></span>Contact Details</h4>
    <p style="line-height:17px">Toll Free (NA): 1-800-555-0142<br>Toll Free (UK): 0800-555-0199<br>Toll Free (Ireland): 1-800-555-017<br>Phone: 416-555-0163</p>
  </div>
  <div class="abs social" style="left:657px"><div class="ic"></div>Blog</div>
  <div class="abs social" style="left:706px"><div class="ic"></div>Video</div>
  <div class="abs social" style="left:755px"><div class="ic"></div>Social</div>
  <div class="abs social" style="left:804px"><div class="ic"></div>Updates</div>

  <div class="abs legal-rule"></div>
  <div class="abs legal"><span>©2012 Bright Harbor</span>•<span>About</span>•<span>Press</span>•<span>Careers</span>•<span>Terms</span>•<span>Privacy Policy</span>•<span>Support</span>•<span>Resources</span></div>
</div>
</body>
</html>
```